Web Design Project

Psychotherapist in Private Practice
Practice name "The Steady Harbor"
The population is professional adults seeking life coaching and change consultation
I am including a photo for inspiration ONLY - It includes the theme of light and tree branches. There does not HAVE to be a photograph . An illustration , concept or theme of nature /light / generativity / growth / creativity is acceptable
Clean sharp lines Light colors, minimalist , modern.
There is a separate project for a logo design that will become part of the web design
Here are examples of two logos/websites I like
http://www.quietrivergroup.example/
http://www.brightknollpartners.example/

Target Market(s)

Professional adults seeking life coaching

Industry/Entity Type

Life Coaching

Requirements
Should not have
• Although the business name has 'compassion' in it, designs with hearts in it would have to be pretty stylish, subtle, mature and sophisticated to be considered.

```html
<!DOCTYPE html>
<html lang="en">
<head>
<meta charset="utf-8">
<title>The Steady Harbor</title>
<link rel="stylesheet" href="https://fonts.googleapis.com/css2?family=Open+Sans:wght@400;600;700&family=Courgette&display=swap">
<style>
:root{
  --nav:#5b4b22;
  --nav-line:#e9dcae;
  --ink:#222;
  --brown:#3a2a08;
  --slide:#c3d3d6;
  --circle-yellow:#f0c84a;
  --circle-green:#b0da76;
  --circle-grey:#d6d6d6;
  --footer:#dcdcdc;
  --footer-box:#e9e9e9;
  --link:#1f5fb0;
  --date:#2a4d8f;
  --muted:#7a7a7a;
}
*{box-sizing:border-box;margin:0;padding:0}
html,body{width:823px;height:1200px;overflow:hidden;background:#fff}
.canvas{position:relative;width:823px;height:1200px;overflow:hidden;font-family:"Open Sans",sans-serif;color:var(--ink);background:#fff}
.abs{position:absolute}
.hero-bg{left:0;top:0;width:823px;height:480px;
  background:linear-gradient(180deg,#fdf6dc 0%,#f7dc73 18%,#f4cf4e 40%,#f9e7a0 75%,rgba(255,255,255,0) 100%)}
.nav{left:0;top:23px;width:823px;height:43px;background:var(--nav);border-bottom:2px dashed var(--nav-line);opacity:.92}
.nav a{position:absolute;top:11px;color:#fff;text-decoration:none;font-size:15px}
.brand{left:218px;top:128px;width:350px;text-align:center;font-size:36px;font-weight:600;color:var(--brown);letter-spacing:.5px}
.tagline{left:200px;top:226px;width:386px;text-align:center;font-family:"Courgette",cursive;font-size:16px;color:#1b1405}
.slide{left:81px;top:310px;width:519px;height:244px;background:var(--slide);border:1px solid #ddd}
.slide-shadow{left:120px;top:548px;width:440px;height:26px;border-radius:50%;background:radial-gradient(ellipse at center,rgba(0,0,0,.55) 0%,rgba(0,0,0,0) 70%)}
.dot{top:564px;width:10px;height:10px;border-radius:50%;background:#111}
.slogan{left:615px;font-family:"Courgette",cursive;font-weight:400;color:#111}
.welcome{left:82px;top:596px;font-family:"Courgette",cursive;font-weight:400;font-size:19px;color:#111}
.portrait{left:80px;top:632px;width:127px;height:91px;background:linear-gradient(135deg,#d9dde2,#b79a85 55%,#5a4a45);border:1px solid #bbb}
.intro{left:228px;top:633px;width:534px;font-size:9.2px;line-height:12.3px}
.intro p+p{margin-top:12px}
.rule{left:81px;top:741px;width:596px;height:1px;background:#e4e4e4}
.read-more{font-size:11.5px;color:#222}
.circle{width:200px;height:200px;border-radius:50%;top:783px}
.circle h2{position:absolute;top:27px;width:100%;text-align:center;font-weight:400;font-size:18px}
.circle p{position:absolute;left:29px;width:150px;font-size:9.2px;line-height:12.3px}
.circle .read-more{position:absolute;top:168px;width:100%;text-align:center;font-size:11px}
.circle-shadow{top:978px;width:130px;height:22px;border-radius:50%;opacity:.7}
.yellow{background:var(--circle-yellow)}
.green{background:var(--circle-green)}
.grey{background:var(--circle-grey)}
.footer{left:0;top:1017px;width:823px;height:183px;background:linear-gradient(180deg,#c8c8c8 0,#e2e2e2 6px,var(--footer) 100%);border-top:2px solid #b4b4b4}
.foot-title{font-size:12.3px;color:#333}
.more-btn{left:239px;top:1041px;width:36px;height:15px;border-radius:8px;background:#555;color:#fff;font-size:6px;line-height:15px;padding-left:7px}
.news{left:96px;width:178px;height:38px;background:var(--footer-box);padding:6px 8px;font-size:8.5px}
.news .head{font-weight:700;color:#333;border-bottom:1px solid #c9c9c9;padding-bottom:2px}
.news .date{color:var(--date)}
.news .by{color:var(--muted);font-style:italic;padding-left:32px;margin-top:2px;font-size:8px}
.vline{width:1px;background:#bdbdbd;top:1037px;height:148px}
.company{left:323px;top:1068px;font-size:9px;color:var(--link);font-weight:600}
.company-rule{left:323px;top:1085px;width:192px;height:1px;background:#bcbcbc}
.address{left:323px;top:1091px;font-size:8.3px;line-height:14.9px;color:#333}
.address a{color:var(--link);text-decoration:none}
.map{left:426px;top:1092px;width:90px;height:65px;border:2px solid #fff;background:#e2e0d6;box-shadow:0 0 2px #999}
.foot-brand{left:563px;top:1017px;width:155px;height:56px;background:var(--brown);color:#fff;font-size:14px;font-weight:600;display:flex;align-items:center;justify-content:center}
.copyright{left:565px;top:1090px;font-size:7.5px;line-height:14px;color:#444}
</style>
</head>
<body>
<div class="canvas">
  <div class="abs hero-bg" role="img" aria-label="Soft golden wheat field glowing in sunlight"></div>

  <nav class="abs nav">
    <a style="left:62px">Home</a>
    <a style="left:132px">Programs</a>
    <a style="left:229px">Success Stories</a>
    <a style="left:360px">Free Resources</a>
    <a style="left:491px">Blog</a>
    <a style="left:553px">Contact Us</a>
    <a style="left:656px">Affiliate Program</a>
  </nav>

  <div class="abs brand">The Steady Harbor</div>
  <div class="abs tagline">seeking life coaching &amp; change consultation</div>

  <div class="abs slide-shadow"></div>
  <div class="abs slide" role="img" aria-label="Slider photo: man in an office chair with arms wide, outdoors in an open field"></div>
  <span class="abs dot" style="left:276px"></span>
  <span class="abs dot" style="left:297px"></span>
  <span class="abs dot" style="left:318px"></span>
  <span class="abs dot" style="left:340px"></span>
  <span class="abs dot" style="left:361px"></span>

  <div class="abs slogan" style="top:315px;font-size:19px">Change Your</div>
  <div class="abs slogan" style="top:350px;font-size:34px">Tinking</div>
  <div class="abs slogan" style="top:404px;font-size:40px">Way</div>
  <div class="abs slogan" style="top:473px;font-size:19px">Change your</div>
  <div class="abs slogan" style="top:505px;font-size:34px">Life</div>

  <h1 class="abs welcome">Welcome The Steady Harbor</h1>
  <div class="abs portrait" role="img" aria-label="Smiling businesswoman with colleagues in the background"></div>
  <div class="abs intro">
    <p>Loren text usedI have discovered one lasting way to truly change yourself. When applied, it will transform you from the inside out and cause you to think and act differently and experience all that life has to offer. Coaching is not therapy, but a partnering relationship that leads to major changes in your life. You will be able to identify the reasons and characteristics that prevent you from living at your peak performance in the midst of life's challenges.</p>
    <p>Human nature cannot be trusted to always do the right thing. Without a solid anchor or foundation, we can drift off course in life and may even crash on the obstacles in our path.</p>
  </div>
  <div class="abs rule"></div>
  <div class="abs read-more" style="left:688px;top:733px">Read More...</div>

  <div class="abs circle-shadow" style="left:115px;background:radial-gradient(ellipse,#8a7a3a 0%,rgba(0,0,0,0) 70%)"></div>
  <div class="abs circle-shadow" style="left:336px;background:radial-gradient(ellipse,#7a8f55 0%,rgba(0,0,0,0) 70%)"></div>
  <div class="abs circle-shadow" style="left:556px;background:radial-gradient(ellipse,#8a8a8a 0%,rgba(0,0,0,0) 70%)"></div>

  <section class="abs circle yellow" style="left:80px">
    <h2>ABOUT US</h2>
    <p style="top:67px">Loren text usedI have discovered one lasting way to truly change yourself.</p>
    <p style="top:116px">When applied, it will transform you from the inside out and cause you to think</p>
    <div class="read-more">Read More...</div>
  </section>
  <section class="abs circle green" style="left:301px">
    <h2>WHAT WE DO</h2>
    <p style="top:67px">Loren text usedI have discovered one lasting way to truly change yourself.</p>
    <p style="top:116px">When applied, it will transform you from the inside out and cause you to think</p>
    <div class="read-more">Read More...</div>
  </section>
  <section class="abs circle grey" style="left:521px">
    <h2>MEMBERSHIP</h2>
    <p style="top:67px">Loren text usedI have discovered one lasting way to truly change yourself.</p>
    <p style="top:116px">When applied, it will transform you from the inside out and cause you to think</p>
    <div class="read-more">Read More...</div>
  </section>

  <footer class="abs footer"></footer>

  <svg class="abs" style="left:100px;top:1030px" width="26" height="32" viewBox="0 0 26 32" aria-hidden="true">
    <rect x="1" y="3" width="24" height="28" rx="2" fill="#fff" stroke="#555"/>
    <rect x="1" y="3" width="24" height="7" fill="#2f5d9a"/>
    <text x="13" y="26" text-anchor="middle" font-family="Open Sans,sans-serif" font-size="12" fill="#222">14</text>
  </svg>
  <div class="abs foot-title" style="left:137px;top:1038px">Latest News</div>
  <div class="abs more-btn">more ▸</div>

  <div class="abs news" style="top:1072px"><div class="head"><span class="date">26/03</span> &nbsp;- &nbsp;Lorem ipsum dolor sit amet</div><div class="by">by admin</div></div>
  <div class="abs news" style="top:1111px"><div class="head"><span class="date">26/03</span> &nbsp;- &nbsp;Lorem ipsum dolor sit amet</div><div class="by">by admin</div></div>
  <div class="abs news" style="top:1150px"><div class="head"><span class="date">26/03</span> &nbsp;- &nbsp;Lorem ipsum dolor sit amet</div><div class="by">by admin</div></div>

  <div class="abs vline" style="left:298px"></div>

  <svg class="abs" style="left:321px;top:1033px" width="34" height="28" viewBox="0 0 34 28" aria-hidden="true">
    <rect x="2" y="4" width="30" height="21" fill="#f4f4f4" stroke="#777"/>
    <path d="M2 4 L17 16 L32 4" fill="none" stroke="#777"/>
  </svg>
  <div class="abs foot-title" style="left:364px;top:1038px">Contact Us</div>
  <div class="abs company">STEADY HARBOR</div>
  <div class="abs company-rule"></div>
  <div class="abs address">
    Lindenlaan 14<br>1234 AB Havenstad<br>The Netherlands<br>T.: 010-5550142<br>F.: 010-5550143<br>E: <a>info@steadyharbor.example</a>
  </div>
  <div class="abs map" role="img" aria-label="Small street map with a location marker"></div>

  <div class="abs vline" style="left:540px"></div>

  <div class="abs foot-brand">The Steady Harbor</div>
  <div class="abs copyright">Copyright © The Steady Harbor<br>All rights reserved.</div>
</div>
</body>
</html>
```